medical equipment home page redesign

We need a new home page for an existing store. We'll be redoing the entire site to make it more user friendly and follow storybrand guidelines. We have a loose wireframe for the sections, but need help making it look great. The look should be clean, modern, professional, etc. We have a background image we would like to incorporate somewhere because we've just printed business cards and brochures that use this background image. We love parallax effects on backgrounds, so please allow extra big background images so we can utilize that effect. You can find images, etc from our site at brivontel.com. We like the way this site feels: http://okmu.fendaro.com/home/page/venue with the parallax background. And this one, too: https://www.tessilmarow.org/

Target Market(s)

people with chronic pain

Industry/Entity Type

Medical Equipment

Number of Pages Required

1 page

Font styles to use
Sans Serif

Colors
b8a6cd
6b449b
e4daeb

Requirements
Must have
• Please include sections from our wireframe. They don't have to look like the wireframe, but they do need to portray that information in each section.
Nice to have
• It would be great if you could include the background image we have attached
Should not have
• Should not look like the old site.

```html
<!DOCTYPE html>
<html lang="en">
<head>
<meta charset="utf-8">
<title>Brivontel – Light Your Way Out Of Pain</title>
<link href="https://fonts.googleapis.com/css2?family=Poppins:wght@300;400;500;600;700&display=swap" rel="stylesheet">
<style>
:root{
  --purple:#6b449b;
  --purple-hero:#6f47a2;
  --lilac:#b8a6cd;
  --lavender:#e4daeb;
  --ink:#1f1f24;
  --muted:#77737e;
  --white:#ffffff;
  --gold:#f5b82e;
  --red:#d4252b;
}
*{box-sizing:border-box;margin:0;padding:0}
html,body{width:1200px;height:4773px;overflow:hidden}
body{font-family:'Poppins',sans-serif;color:var(--ink);background:var(--white);position:relative}
.abs{position:absolute}

/* header */
.site-header{position:absolute;left:0;top:0;width:1200px;height:88px;background:var(--white)}
.brand{position:absolute;left:88px;top:20px;display:flex;align-items:center;gap:10px}
.brand-dot{width:14px;height:14px;border-radius:50%;background:var(--red)}
.brand-name{font-size:26px;font-weight:600;color:var(--purple)}
.nav{position:absolute;right:90px;top:22px;display:flex;align-items:center;gap:34px;font-size:12.5px;font-weight:500;letter-spacing:.3px}
.nav a{color:var(--ink);text-decoration:none}
.nav .shop{background:var(--lilac);color:var(--white);padding:13px 22px;font-size:11.5px}

/* hero */
.hero{position:absolute;left:0;top:88px;width:1200px;height:609px;background:var(--purple-hero);overflow:hidden}
.hero-word{position:absolute;left:-20px;top:10px;font-size:360px;font-weight:700;color:rgba(255,255,255,.06);line-height:1;writing-mode:vertical-rl;transform:rotate(180deg)}
.hero-visual{position:absolute;left:120px;top:95px;width:426px;height:426px;border-radius:50%;background:radial-gradient(circle at 60% 35%,#f3b98a 0%,#c77a74 35%,#6d5fa7 70%,#4a3f8c 100%)}
.hero h1{position:absolute;left:613px;top:160px;font-size:64px;font-weight:500;line-height:1.05;color:var(--white);letter-spacing:.5px}
.hero .lead{position:absolute;left:613px;top:310px;width:470px;font-size:22px;line-height:1.2;color:var(--white);font-weight:300}
.hero .btn{position:absolute;left:615px;top:390px;width:147px;height:49px;background:var(--lilac);color:var(--white);font-size:13px;font-weight:600;display:flex;align-items:center;justify-content:center;letter-spacing:.4px}
.slide-count{position:absolute;left:1140px;top:290px;color:var(--white);text-align:center;width:30px}
.slide-count .cur{font-size:15px}
.slide-count .line{width:1px;height:50px;background:rgba(255,255,255,.5);margin:10px auto}
.slide-count .tot{font-size:21px;font-weight:600}

/* benefits */
.benefits{position:absolute;left:0;top:697px;width:1200px;height:85px;background:var(--lavender);display:flex}
.benefit{flex:1;display:flex;align-items:center;justify-content:center;gap:10px;font-size:26px;font-weight:500;color:var(--purple);border-right:2px solid #fff}
.benefit:last-child{border-right:0}

/* section headings */
.section-title{position:absolute;font-size:37px;font-weight:500;color:var(--ink)}
.center{width:1200px;left:0;text-align:center}

/* product cards */
.product{position:absolute;width:250px;height:292px;background:var(--white);box-shadow:0 18px 40px rgba(70,40,110,.10);text-align:center}
.product .thumb{margin:40px auto 0;width:180px;height:128px;border-radius:6px}
.product .name{margin-top:30px;font-size:14.5px;color:var(--ink)}
.product .price{margin-top:6px;font-size:17px;font-weight:600;color:var(--purple)}
.thumb-pbm{background:linear-gradient(135deg,#5a5a60,#2a2a2e 55%,#e6d8e6)}
.thumb-red{background:linear-gradient(135deg,#222,#5a5a60 50%,#c94a6b)}
.thumb-green{background:linear-gradient(135deg,#222,#5a5a60 50%,#3e8f63)}
.thumb-kit{background:linear-gradient(135deg,#3a2d55,#6b5a8c 45%,#e8c9b2)}

/* testimonials */
.band{position:absolute;left:0;width:1200px;background:var(--lavender);overflow:hidden}
.quote{position:absolute;width:400px;height:240px;background:var(--white);padding:52px 28px 0}
.quote p{font-size:14px;line-height:1.6;color:var(--muted);font-weight:300}
.quote .meta{position:absolute;left:28px;right:28px;top:168px;border-top:1px solid #e6e2ea;padding-top:14px}
.quote .who{font-size:16px;font-weight:600}
.quote .role{font-size:13px;color:var(--muted)}
.quote .stars{position:absolute;right:0;top:22px;color:var(--gold);font-size:17px;letter-spacing:1px}
.quote .stars .off{color:#e3e0e6}
.avatar{position:absolute;width:78px;height:78px;border-radius:50%;top:-40px;left:28px}
.dots{position:absolute;top:1800px;left:0;width:1200px;display:flex;justify-content:center;gap:8px}
.dots span{width:9px;height:9px;border-radius:50%;border:1.5px solid #8b8790}
.dots span.on{background:#8b8790}

/* pets */
.tile{position:absolute;top:2058px;width:332px;height:292px;display:flex;align-items:flex-end;justify-content:center;padding-bottom:28px;color:var(--white);font-size:30px;font-weight:600}

/* arrows */
.arrow{position:absolute;width:36px;height:36px;border-radius:50%;background:var(--white);box-shadow:0 4px 14px rgba(0,0,0,.12);display:flex;align-items:center;justify-content:center}

/* video */
.video-word{position:absolute;left:78px;top:3200px;font-size:196px;font-weight:700;color:var(--white);line-height:1;letter-spacing:2px;text-shadow:0 0 1px rgba(0,0,0,.03)}
.video-title{position:absolute;left:90px;top:3385px;font-size:46px;font-weight:500;line-height:1.17}
.video-frame{position:absolute;left:521px;top:3120px;width:679px;height:555px;background:linear-gradient(90deg,#c8b8a6 0%,#6e4b9e 35%,#a3383c 65%,#4fb3cc 100%)}
.play{position:absolute;left:809px;top:3346px;width:104px;height:104px;border-radius:50%;background:var(--white);display:flex;align-items:center;justify-content:center}

/* blog */
.post{position:absolute;top:3847px;width:323px;height:451px;background:var(--white);box-shadow:0 18px 40px rgba(70,40,110,.10)}
.post .img{height:222px}
.post .body{padding:24px 24px 0}
.post .date{display:inline-block;background:var(--lavender);color:var(--purple);font-size:11px;padding:3px 8px}
.post h3{margin-top:14px;font-size:15.5px;font-weight:600;line-height:1.3;min-height:40px}
.post p{margin-top:14px;font-size:13px;line-height:1.7;color:var(--muted);font-weight:300}

/* newsletter */
.newsletter{position:absolute;left:0;top:4398px;width:1200px;height:375px;background:var(--purple-hero);color:var(--white)}
.newsletter h2{position:absolute;left:0;width:1200px;top:74px;text-align:center;font-size:44px;font-weight:500}
.field{position:absolute;top:115px}
.field label{display:block;font-size:11px;font-weight:600;margin-bottom:6px}
.field .input{width:298px;height:47px;background:var(--white);color:#8a8690;font-size:13px;padding:15px 16px}
.signup{position:absolute;left:846px;top:168px;width:136px;height:47px;background:var(--lavender);color:var(--ink);font-size:15px;font-weight:600;display:flex;align-items:center;justify-content:center}
.foot-line{position:absolute;left:88px;top:320px;width:1024px;height:1px;background:rgba(255,255,255,.35)}
.copyright{position:absolute;left:0;width:1200px;top:340px;text-align:center;font-size:11.5px;font-weight:500}
.to-top{position:absolute;left:1137px;top:284px;width:40px;height:40px;border-radius:50%;background:var(--white);display:flex;align-items:center;justify-content:center}
</style>
</head>
<body>

<header class="site-header">
  <div class="brand"><span class="brand-dot"></span><span class="brand-name">Brivontel</span></div>
  <nav class="nav">
    <a href="#">HOME</a><a href="#">WHAT'S NEW?</a><a href="#">ABOUT US</a><a href="#" class="shop">SHOP NOW</a>
  </nav>
</header>

<section class="hero">
  <div class="hero-word">LIGHT</div>
  <div class="hero-visual" role="img" aria-label="Four therapy flashlights with red, blue and green tips over a sunset sky"></div>
  <h1>Light Your Way<br>Out Of Pain</h1>
  <p class="lead">Because everyone deserves access to a pain free life</p>
  <div class="btn">SHOP NOW</div>
  <div class="slide-count"><div class="cur">02</div><div class="line"></div><div class="tot">05</div></div>
</section>

<section class="benefits">
  <div class="benefit">
    <svg width="50" height="46" viewBox="0 0 50 46"><rect x="4" y="8" width="26" height="14" rx="7" transform="rotate(-40 17 15)" fill="none" stroke="#6b449b" stroke-width="3"/><circle cx="30" cy="30" r="12" fill="#6b449b"/><line x1="22" y1="38" x2="38" y2="22" stroke="#e4daeb" stroke-width="3"/></svg>
    Drug Free</div>
  <div class="benefit">
    <svg width="44" height="46" viewBox="0 0 44 46"><path d="M22 3 L39 9 V22 C39 33 31 40 22 43 C13 40 5 33 5 22 V9 Z" fill="none" stroke="#6b449b" stroke-width="3"/><path d="M14 23 L20 29 L31 17" fill="none" stroke="#6b449b" stroke-width="3.5"/></svg>
    Safe</div>
  <div class="benefit">
    <svg width="56" height="46" viewBox="0 0 56 46"><circle cx="44" cy="10" r="8" fill="#6b449b"/><path d="M6 16 L34 20 L22 30 Z" fill="#6b449b"/><rect x="18" y="28" width="6" height="14" fill="#6b449b"/></svg>
    Pain Relief</div>
</section>

<h2 class="section-title" style="left:86px;top:876px">How Light Therapy Can Stop Your Pain</h2>
<div class="product" style="left:88px;top:945px"><div class="thumb thumb-pbm" role="img" aria-label="Grey PBM flashlight with charger"></div><div class="name">BRV PBM Light w/Charger</div><div class="price">$599.00</div></div>
<div class="product" style="left:346px;top:945px"><div class="thumb thumb-red" role="img" aria-label="Red light flashlight with pouch and bonus"></div><div class="name">BRV Red Light + Bonus</div><div class="price">$329.00</div></div>
<div class="product" style="left:604px;top:945px"><div class="thumb thumb-green" role="img" aria-label="Green light flashlight with pouch and bonus"></div><div class="name">BRV Green Light + Bonus</div><div class="price">$329.00</div></div>
<div class="product" style="left:860px;top:945px"><div class="thumb thumb-kit" role="img" aria-label="Complete package with bag, lights and guides"></div><div class="name">Complete Package</div><div class="price">$399.00 – $518.00</div></div>

<section class="band" style="top:1343px;height:550px">
  <h2 class="section-title center" style="top:88px">Testimonials</h2>
  <div class="quote" style="left:88px;top:187px">
    <div class="avatar" style="background:linear-gradient(135deg,#c9a08a,#7b6a64)" role="img" aria-label="Customer portrait"></div>
    <p>Etiam rhoncus maecenas tempus, tellus eget condim entum rhon cus sem quam semper libero amet adipisc ing sem neque sed ipsum nam quam nunc.</p>
    <div class="meta"><div class="who">Marisol</div><div class="role">Founder at Quarrow</div><div class="stars">★★★★<span class="off">★</span></div></div>
  </div>
  <div class="quote" style="left:524px;top:187px">
    <div class="avatar" style="background:linear-gradient(135deg,#3fc6c9,#c86a52)" role="img" aria-label="Customer portrait"></div>
    <p>Etiam rhoncus maecenas tempus, tellus eget condim entum rhon cus sem quam semper libero amet adipisc ing sem neque sed ipsum nam quam nunc.</p>
    <div class="meta"><div class="who">Dario Quell</div><div class="role">Founder at Velmora</div><div class="stars">★★★★<span class="off">★</span></div></div>
  </div>
  <div class="quote" style="left:960px;top:187px">
    <div class="avatar" style="background:linear-gradient(135deg,#4d4f57,#e3b13a)" role="img" aria-label="Customer portrait"></div>
    <p>Etiam rhoncus maecenas tempus, tellus eget condim entum rhon cus sem quam semper libero amet adipisc ing sem neque sed ipsum nam quam nunc.</p>
    <div class="meta"><div class="who">Anika Verro</div><div class="role">Founder at Stonequill</div></div>
  </div>
</section>
<div class="dots"><span class="on"></span><span></span><span></span></div>

<h2 class="section-title" style="left:88px;top:1992px">Light Therapy For You &amp; Your Pets</h2>
<div class="tile" style="left:88px;background:linear-gradient(160deg,#4a4a44,#2c302a 60%,#5b5a4c)" role="img" aria-label="Bearded man in green shirt">People</div>
<div class="tile" style="left:433px;background:linear-gradient(160deg,#5a3a24,#a66a3a 50%,#3b2616)" role="img" aria-label="Golden dog lying in autumn leaves">Dogs</div>
<div class="tile" style="left:778px;background:linear-gradient(180deg,#c9c4b6,#8d7b5e 55%,#4a3a28)" role="img" aria-label="Horses standing in a field">Horses</div>

<section class="band" style="top:2458px;height:555px">
  <h2 class="section-title center" style="top:88px">Featured Products</h2>
</section>
<div class="product" style="left:88px;top:2612px"><div class="thumb thumb-pbm" role="img" aria-label="Grey PBM flashlight with charger"></div><div class="name">BRV PBM Light w/Charger</div><div class="price">$599.00</div></div>
<div class="product" style="left:346px;top:2612px"><div class="thumb thumb-red" role="img" aria-label="Red light flashlight with pouch and bonus"></div><div class="name">BRV Red Light + Bonus</div><div class="price">$329.00</div></div>
<div class="product" style="left:604px;top:2612px"><div class="thumb thumb-green" role="img" aria-label="Green light flashlight with pouch and bonus"></div><div class="name">BRV Green Light + Bonus</div><div class="price">$329.00</div></div>
<div class="product" style="left:860px;top:2612px"><div class="thumb thumb-kit" role="img" aria-label="Complete package with bag, lights and guides"></div><div class="name">Complete Package...</div><div class="price">$399.00 – $518.00</div></div>
<div class="arrow" style="left:26px;top:2740px"><svg width="14" height="10" viewBox="0 0 14 10"><path d="M13 5H2M5 1L1 5l4 4" fill="none" stroke="#333" stroke-width="1.4"/></svg></div>
<div class="arrow" style="left:1138px;top:2740px"><svg width="14" height="10" viewBox="0 0 14 10"><path d="M1 5h11M9 1l4 4-4 4" fill="none" stroke="#333" stroke-width="1.4"/></svg></div>

<div class="video-frame" role="img" aria-label="Two women talking about the therapy lights outdoors"></div>
<div class="video-word">VIDEO</div>
<h2 class="video-title">A Very<br>Information Video<br>About The Lights</h2>
<div class="play"><svg width="30" height="32" viewBox="0 0 30 32"><path d="M4 2 L28 16 L4 30 Z" fill="#111"/></svg></div>

<h2 class="section-title center" style="top:3770px">Our Blog</h2>
<article class="post" style="left:88px">
  <div class="img" style="background:linear-gradient(135deg,#5a4a3e,#2b2622 50%,#b9b3a8)" role="img" aria-label="Horse wearing a red halter"></div>
  <div class="body"><span class="date">Feb 21, 2020</span><h3>Best Practices-Don't<br>Cross-Tie</h3><p>When we show people how to use their Brivontel Lights with their horses, we stress how important it is to listen to the horse...</p></div>
</article>
<article class="post" style="left:439px">
  <div class="img" style="background:linear-gradient(135deg,#8a8580,#d8cfc4 50%,#5f5a55)" role="img" aria-label="Person holding a knee in pain"></div>
  <div class="body"><span class="date">Feb 21, 2020</span><h3>What is Photobiomodulation Therapy? (PBMT)</h3><p>Photobiomodulation therapy (PBMT) is defined as a form of light therapy that utilizes non-ionizing light sources. This type of therapy...</p></div>
</article>
<article class="post" style="left:789px">
  <div class="img" style="background:linear-gradient(90deg,#1a1020,#d2338e 30%,#3a4fd8 55%,#2fc37a 80%,#0e1a14)" role="img" aria-label="Three lights glowing pink, blue and green"></div>
  <div class="body"><span class="date">Feb 21, 2020</span><h3>BRV Light Dosing</h3><p>Please use the following charts to determine the amount of energy (Joules) the Brivontel Lights are delivering. For more information regarding dosing, check out this page.</p></div>
</article>

<footer class="newsletter">
  <h2>Join Our Newsletter</h2>
  <div class="field" style="left:218px"><label>NAME*</label><div class="input">Enter your name</div></div>
  <div class="field" style="left:522px"><label>EMAIL*</label><div class="input">Enter your email</div></div>
  <div class="signup">SIGN UP</div>
  <div class="to-top"><svg width="10" height="14" viewBox="0 0 10 14"><path d="M5 13V2M1 5l4-4 4 4" fill="none" stroke="#333" stroke-width="1.4"/></svg></div>
  <div class="foot-line"></div>
  <div class="copyright">© COPYRIGHT 2020 ALL RIGHTS RESERVED</div>
</footer>

</body>
</html>
```